PennantVoyage

1. Can you describe what your company does?

Please find enclosed documents for your reference about our business doing.

2. Who are your target customers for the website?

Company Positioning: A comprehensive supplier of premier international sports travel and high-end event services.
Core Advantage: Exclusive international partnership resources and an Official Ticketing Assurance System.
Service Standard: One-Stop, High-Quality Service Solutions based on the "An once-in-a-lifetime experience" philosophy.

Our target customers for the website:
Mid-to-High-end Sports Enthusiasts
Corporate Clients
Sports Associations
Please kindly find enclosed for more details about our target customers, I think it's very important to make it clear to you.

3. Do you have an existing domain name / website address?

Yes, I have. I just applied for this new domain and it's totally a new website. www.pennantvoyage.com

4. In addition to a Home Page, which other pages / sections would you like your website to have:
About Us
Contact Us , Office / Mailing Address
Sports Travel Products( Bucket Lists) : Vessel Meet, Amber Round, Heliads, Football, KLQ, Golf, Skiing, Hiking,Galas
Reviews/ Unforgettable Moments
FAQs
Any other page / section you would like: Here is the website for your reference, www.laneweaver.com
For each of the pages / sections you’d like to have, please provide the text (and images, if available) you would like to include.
Please recommend 2-3 templates to me, and let me know what kind of text I will provide to every web pages.

5. Which of the below are features and functionalities your website will need:
Image Gallery
Videos
Contact Form
Maps
FAQs
6. Please provide the URLs for the social media profiles you'd like to link to the website.

Do you know Quiet Blue Ledger?

Please let me know anything you need, thank you very much!

Have a good day!

Target Market(s)

Travel for the world-wide sports games and make an once-in-a-lifetime experience

Industry/Entity Type

sports and travel industry

Coding

Coded - Design and coding required

Number of Pages Required

5+ page

Requirements
Must have
• our logo
Nice to have
• On the homepage, I’d like a banner-style section to prominently showcase the latest products.

```html
<!DOCTYPE html>
<html lang="en">
<head>
<meta charset="utf-8">
<title>PennantVoyage – Sports Travel</title>
<link rel="stylesheet" href="https://fonts.googleapis.com/css2?family=Montserrat:wght@600;700;800;900&family=Open+Sans:wght@400;600&display=swap">
<style>
  :root {
    --ink-dark: #1c2533;
    --ink-deeper: #121a26;
    --accent-red: #ee3d4f;
    --accent-red-soft: #f05a66;
    --gold: #f5b800;
    --white: #ffffff;
    --text-soft: #e6e9ee;
    --label-grey: #d8dce2;
    --menu-black: #000000;
    --rule: rgba(255,255,255,0.14);
  }
  * { margin: 0; padding: 0; box-sizing: border-box; }
  html, body { width: 1200px; height: 708px; overflow: hidden; }
  body { font-family: "Montserrat", sans-serif; color: var(--white); background: var(--ink-dark); }

  .hero { position: relative; width: 1200px; height: 708px; overflow: hidden; }
  .hero-backdrop {
    position: absolute; inset: 0;
    background:
      radial-gradient(ellipse at 80% 40%, rgba(90,110,140,0.55), transparent 60%),
      radial-gradient(ellipse at 15% 75%, rgba(60,80,105,0.5), transparent 55%),
      linear-gradient(180deg, #2a3647 0%, #232e3e 55%, #1b2431 100%);
  }
  .deco-circle { position: absolute; border-radius: 50%; background: rgba(255,255,255,0.14); }

  .site-header {
    position: absolute; left: 0; top: 0; width: 1200px; height: 124px;
    border-bottom: 1px solid var(--rule);
  }
  .brand {
    position: absolute; left: 100px; top: 44px;
    display: flex; align-items: center; gap: 8px;
    font-weight: 800; font-size: 19px; color: var(--accent-red);
  }
  .brand-mark { width: 14px; height: 14px; background: var(--accent-red); }

  .main-nav a, .lang-switch {
    position: absolute; top: 43px; height: 34px;
    display: flex; align-items: center; justify-content: center;
    font-size: 12px; font-weight: 600; color: var(--white); text-decoration: none;
  }
  .nav-pill { background: var(--accent-red-soft); border-radius: 17px; }
  .nav-home { left: 358px; width: 58px; }
  .nav-sports { left: 424px; width: 120px; gap: 4px; }
  .nav-packages { left: 563px; }
  .nav-about { left: 699px; }
  .nav-contact { left: 782px; }
  .lang-switch { left: 881px; gap: 5px; font-size: 11px; }
  .btn-book {
    position: absolute; left: 972px; top: 43px; width: 110px; height: 34px;
    border-radius: 17px; background: var(--accent-red);
    display: flex; align-items: center; justify-content: center;
    font-size: 11px; font-weight: 700; letter-spacing: 1px; color: var(--white);
    box-shadow: 0 6px 16px rgba(238,61,79,0.35);
  }

  .sports-menu {
    position: absolute; left: 425px; top: 79px; width: 173px; height: 231px;
    background: var(--menu-black); border-radius: 4px; z-index: 5;
    list-style: none; padding: 16px 0 0 19px;
  }
  .sports-menu li { height: 35px; font-size: 10.5px; font-weight: 700; line-height: 1; padding-top: 4px; }

  .hero-title {
    position: absolute; left: 0; top: 150px; width: 1200px; text-align: center;
    font-weight: 900; font-size: 52px; line-height: 56px; letter-spacing: 0.5px;
  }
  .hero-title .hl { color: var(--accent-red); }
  .hero-lede {
    position: absolute; left: 310px; top: 340px; width: 580px; text-align: center;
    font-family: "Open Sans", sans-serif; font-size: 17px; line-height: 27px; color: var(--text-soft);
  }

  .btn {
    position: absolute; top: 437px; height: 45px; border-radius: 23px;
    display: flex; align-items: center; justify-content: center; gap: 7px;
    font-size: 11px; font-weight: 700; letter-spacing: 1px;
  }
  .btn-primary { left: 338px; width: 274px; background: var(--accent-red); color: var(--white); box-shadow: 0 8px 20px rgba(238,61,79,0.35); }
  .btn-outline { left: 629px; width: 237px; border: 1px solid var(--accent-red); color: var(--accent-red); }

  .stats { position: absolute; top: 545px; left: 0; width: 1200px; }
  .stat { position: absolute; width: 200px; margin-left: -100px; text-align: center; }
  .stat-rule { width: 42px; height: 2px; background: var(--gold); margin: 0 auto; }
  .stat-value { margin-top: 18px; font-size: 36px; font-weight: 800; color: var(--gold); line-height: 40px; }
  .stat-label { margin-top: 14px; font-family: "Open Sans", sans-serif; font-size: 13px; font-weight: 600; letter-spacing: 0.8px; color: var(--label-grey); }
</style>
</head>
<body>
<section class="hero">
  <div class="hero-backdrop" role="img" aria-label="Photo of cheering fans in a packed tennis stadium with players on court, under a dark overlay"></div>
  <span class="deco-circle" style="left:121px;top:152px;width:56px;height:56px"></span>
  <span class="deco-circle" style="left:845px;top:296px;width:70px;height:70px"></span>
  <span class="deco-circle" style="left:963px;top:465px;width:86px;height:86px"></span>
  <span class="deco-circle" style="left:240px;top:613px;width:42px;height:42px"></span>

  <header class="site-header">
    <div class="brand"><span class="brand-mark"></span>PennantVoyage</div>
    <nav class="main-nav">
      <a class="nav-pill nav-home" href="#">Home</a>
      <a class="nav-pill nav-sports" href="#">Featured Sports
        <svg width="9" height="9" viewBox="0 0 10 10"><path d="M2 3.5l3 3 3-3" fill="none" stroke="#fff" stroke-width="1.6"/></svg>
      </a>
      <a class="nav-packages" href="#">Packages &amp; Service</a>
      <a class="nav-about" href="#">About Us</a>
      <a class="nav-contact" href="#">Contact Us</a>
    </nav>
    <div class="lang-switch">
      <svg width="11" height="11" viewBox="0 0 12 12" fill="none" stroke="#fff" stroke-width="1.1"><circle cx="6" cy="6" r="5"/><ellipse cx="6" cy="6" rx="2.2" ry="5"/><path d="M1 6h10"/></svg>
      English
      <svg width="9" height="9" viewBox="0 0 10 10"><path d="M2 3.5l3 3 3-3" fill="none" stroke="#fff" stroke-width="1.6"/></svg>
    </div>
    <div class="btn-book">BOOK NOW</div>
  </header>

  <ul class="sports-menu">
    <li>Vessel Meet</li>
    <li>Amber Round Tennis</li>
    <li>Heliads</li>
    <li>KLQ Basketball</li>
    <li>Golf Majors</li>
    <li>Marathon Events</li>
  </ul>

  <h1 class="hero-title">AN ONCE-IN-A-LIFETIME<br><span class="hl">EXPERIENCE FOR</span><br><span class="hl">SPORTS</span> TRAVEL</h1>
  <p class="hero-lede">You premier partner for exclusive international sports travel and high-end Event service all around the world!</p>

  <div class="btn btn-primary">EXPLORE PREMIUM PACKAGES
    <svg width="10" height="10" viewBox="0 0 10 10" fill="none" stroke="#fff" stroke-width="1.6"><path d="M1 5h8M6 2l3 3-3 3"/></svg>
  </div>
  <div class="btn btn-outline">VIEW LATEST PACKAGES
    <svg width="10" height="10" viewBox="0 0 10 10" fill="none" stroke="#ee3d4f" stroke-width="1.6"><path d="M1 5h8M6 2l3 3-3 3"/></svg>
  </div>

  <div class="stats">
    <div class="stat" style="left:346px"><div class="stat-rule"></div><div class="stat-value">5,000+</div><div class="stat-label">HAPPY CLIENTS</div></div>
    <div class="stat" style="left:510px"><div class="stat-rule"></div><div class="stat-value">150+</div><div class="stat-label">GLOBAL EVENTS</div></div>
    <div class="stat" style="left:679px"><div class="stat-rule"></div><div class="stat-value">97%</div><div class="stat-label">SATISFACTION RATE</div></div>
    <div class="stat" style="left:858px"><div class="stat-rule"></div><div class="stat-value">14</div><div class="stat-label">YEARS EXPERIENCE</div></div>
  </div>
</section>
</body>
</html>
```